Global Expert Network Firm needs business card design

We need business card design for a new company based in Seoul, South Korea called 'Corwell Insight Partners'. We recruit industry experts covering all countries and connect our client and recruited expert by phone, face-to-face meetings and etc. We are a global expert network firm that is focused on delivering high-quality experts to our clients throughout the world. Our clients include multinational corporations, global consulting firms, private equity firms, venture capital firms, asset management companies.
We have made new logo and please find attachment.(Please use new logo)
Target Market(s)
Global Consulting Firms, Investment Firms, Private Equity Firms, Venture Capital Firms.
Industry/Entity Type
Recruitment
Contact Information for Business Card
We need two Languages (English and Korean Version).
The front is Korean and the back is English version.
[The back] [English]
Company Name: Corwell Insight Partners, Inc.
CEO Name: Daniel Park
Address: #507, Hanbit Bldg, 82 Maebongsan-ro, Dobong-gu, Seoul, 01327, Korea
Tel. +82 2 718 4052
Fax. +82 2 864 1097
Mobile. +82 10 7264 8815
Email: daniel@corwellip.com
Web: www.corwellip.com
[The front] [Korean] => Described in same order as English version.
회사명: 코웰인사이트파트너스(주)
대표이사: 박도현
주소: 서울시 도봉구 매봉산로 82 한빛빌딩 507호
Tel. 02 718 4052
Fax. 02 864 1097
Mobile. 010 7264 8815
Web: www.corwellip.com
Look and feel
Each slider illustrates characteristics of the customer's brand and the style your logo design should communicate.

```html
<!DOCTYPE html>
<html lang="en">
<head>
<meta charset="utf-8">
<title>Corwell Insight Partners — Business Cards</title>
<link href="https://fonts.googleapis.com/css2?family=Noto+Sans+KR:wght@400;500;700&display=swap" rel="stylesheet">
<style>
  :root {
    --backdrop: #dcdcdc;
    --card-black: #1c1c1e;
    --card-black-light: #2e2e31;
    --card-navy: #1c2463;
    --card-navy-light: #34418f;
    --text-white: #ffffff;
    --accent-blue: #3ea6f0;
    --rule-grey: #8a8d96;
    --rule-navy: #7d84b4;
  }
  * { margin: 0; padding: 0; box-sizing: border-box; }
  html, body { width: 1200px; height: 800px; overflow: hidden; }
  body {
    background: var(--backdrop);
    font-family: "Noto Sans KR", Arial, sans-serif;
    position: relative;
  }
  .card {
    position: absolute;
    top: 268px;
    width: 408px;
    height: 264px;
    color: var(--text-white);
    overflow: hidden;
  }
  .card--english {
    left: 130px;
    background: radial-gradient(ellipse 260px 140px at 150px 20px, var(--card-black-light), var(--card-black) 70%);
  }
  .card--korean {
    left: 662px;
    background: radial-gradient(ellipse 300px 220px at 150px 20px, var(--card-navy-light), var(--card-navy) 75%);
  }
  .brand {
    position: absolute;
    left: 296px;
    top: 18px;
    width: 104px;
    display: flex;
    align-items: flex-start;
    gap: 7px;
  }
  .brand__square {
    flex: none;
    width: 10px;
    height: 10px;
    margin-top: 4px;
    background: var(--text-white);
  }
  .brand__name {
    font-size: 13px;
    font-weight: 500;
    line-height: 18px;
    letter-spacing: 0.6px;
    text-transform: uppercase;
    color: var(--text-white);
  }
  .holder {
    position: absolute;
    left: 15px;
    top: 88px;
  }
  .holder__name {
    font-size: 14px;
    font-weight: 700;
    letter-spacing: -0.6px;
    line-height: 18px;
  }
  .card--korean .holder__name { font-weight: 500; letter-spacing: -0.3px; }
  .holder__company {
    font-size: 10px;
    color: var(--accent-blue);
    letter-spacing: -0.4px;
    line-height: 13px;
  }
  .divider {
    position: absolute;
    left: 15px;
    right: 7px;
    top: 123px;
    height: 1px;
    background: var(--rule-grey);
  }
  .card--korean .divider { background: var(--rule-navy); }
  .contacts {
    position: absolute;
    left: 16px;
    top: 135px;
    list-style: none;
  }
  .contacts__item {
    display: flex;
    align-items: center;
    height: 19px;
    font-size: 10px;
    letter-spacing: -0.5px;
  }
  .contacts__icon {
    width: 12px;
    height: 12px;
    margin-right: 7px;
    fill: none;
    stroke: var(--text-white);
    stroke-width: 1.2;
  }
  .contacts__icon--solid { fill: var(--text-white); stroke: none; }
  .contacts__sep { margin: 0 7px; }
  .address {
    position: absolute;
    left: 18px;
    top: 222px;
    font-size: 8px;
    line-height: 10px;
    color: var(--accent-blue);
    letter-spacing: -0.4px;
    text-transform: uppercase;
  }
  .card--korean .address {
    font-size: 10px;
    line-height: 13px;
    top: 219px;
    text-transform: none;
    letter-spacing: -0.3px;
  }
  .icon-sprite { position: absolute; width: 0; height: 0; }
</style>
</head>
<body>

<svg class="icon-sprite" aria-hidden="true">
  <symbol id="icon-phone" viewBox="0 0 12 12">
    <path d="M2.2 1h2l.8 2.6-1.3 1a6.5 6.5 0 0 0 3.1 3.1l1-1.3 2.6.8v2c0 .6-.5 1-1 1A9.6 9.6 0 0 1 1.2 2c0-.5.4-1 1-1z"/>
  </symbol>
  <symbol id="icon-fax" viewBox="0 0 12 12">
    <path d="M1 4h2v7H1zM3.6 5h7.4v6H3.6zM5 1h4.5v3.4H5z"/>
  </symbol>
  <symbol id="icon-globe" viewBox="0 0 12 12">
    <circle cx="6" cy="6" r="5"/>
    <ellipse cx="6" cy="6" rx="2.2" ry="5"/>
    <path d="M1 6h10M2 3.3h8M2 8.7h8"/>
  </symbol>
  <symbol id="icon-mail" viewBox="0 0 12 12">
    <rect x="0.8" y="2.3" width="10.4" height="7.4"/>
    <path d="M0.8 2.3 6 6.8l5.2-4.5M0.8 9.7 4.5 5.6M11.2 9.7 7.5 5.6"/>
  </symbol>
</svg>

<section class="card card--english" aria-label="English side">
  <div class="brand">
    <span class="brand__square"></span>
    <span class="brand__name">Corwell Insight Partners</span>
  </div>
  <div class="holder">
    <p class="holder__name">DANIEL PARK, CEO</p>
    <p class="holder__company">Corwell Insight Partners, Inc.</p>
  </div>
  <div class="divider"></div>
  <ul class="contacts">
    <li class="contacts__item"><svg class="contacts__icon contacts__icon--solid"><use href="#icon-phone"/></svg>+82 2 718 4052<span class="contacts__sep">|</span>+82 10 7264 8815</li>
    <li class="contacts__item"><svg class="contacts__icon contacts__icon--solid"><use href="#icon-fax"/></svg>+82 2 864 1097</li>
    <li class="contacts__item"><svg class="contacts__icon"><use href="#icon-globe"/></svg>www.corwellip.com</li>
    <li class="contacts__item"><svg class="contacts__icon"><use href="#icon-mail"/></svg>daniel@corwellip.com</li>
  </ul>
  <p class="address">#507, Hanbit Bldg, 82 Maebongsan-ro,<br>Dobong-gu, Seoul, 01327, Korea</p>
</section>

<section class="card card--korean" aria-label="Korean side">
  <div class="brand">
    <span class="brand__square"></span>
    <span class="brand__name">Corwell Insight Partners</span>
  </div>
  <div class="holder">
    <p class="holder__name">박도현, 대표이사</p>
    <p class="holder__company">코웰인사이트파트너스(주)</p>
  </div>
  <div class="divider"></div>
  <ul class="contacts">
    <li class="contacts__item"><svg class="contacts__icon contacts__icon--solid"><use href="#icon-phone"/></svg>+82 2 718 4052<span class="contacts__sep">|</span>+82 10 7264 8815</li>
    <li class="contacts__item"><svg class="contacts__icon contacts__icon--solid"><use href="#icon-fax"/></svg>+82 2 864 1097</li>
    <li class="contacts__item"><svg class="contacts__icon"><use href="#icon-globe"/></svg>www.corwellip.com</li>
    <li class="contacts__item"><svg class="contacts__icon"><use href="#icon-mail"/></svg>daniel@corwellip.com</li>
  </ul>
  <p class="address">서울시 도봉구 매봉산로 82<br>한빛빌딩 507호</p>
</section>

</body>
</html>
```